Seven Rising Steps - Site signage graphic

I need a large board creating to show our Seven Bright Paths plan.

I have added a previous version of this called Seven Bold Moves as well as the draft (AI) version of Seven Rising Steps and our new PowerPoint as an example of branding .

Target Market(s)

Colleagues and visitors to site

Industry/Entity Type

Food manufacturing

Font styles to use
Other font styles liked:
• Raleway Medium

Requirements
Must have
• Clear and all text as per AI mock up

```html
<!DOCTYPE html>
<html lang="en">
<head>
<meta charset="utf-8">
<title>Seven Bright Paths – Site Signage</title>
<link rel="stylesheet" href="https://fonts.googleapis.com/css2?family=Montserrat:wght@400;500;700;800;900&family=Oswald:wght@500;600;700&family=Kalam:wght@400&display=swap">
<style>
  :root{
    --green:#1f6b45;
    --green-deep:#1a5d3c;
    --orange:#ec8a1d;
    --cream:#f1eee6;
    --cream-light:#faf8f3;
    --ink:#141414;
    --grey:#6d6d6d;
    --yellow:#f3d54a;
    --white:#ffffff;
  }
  *{box-sizing:border-box;margin:0;padding:0}
  html,body{width:1200px;height:600px;overflow:hidden;background:#dcdcdc}
  .board{position:relative;width:1200px;height:600px;background:var(--cream);overflow:hidden;font-family:"Montserrat",sans-serif}

  /* brand corner */
  .brand-disc{position:absolute;left:-40px;top:-90px;width:230px;height:230px;border-radius:50%;background:var(--cream-light)}
  .brand-name{position:absolute;left:46px;top:42px;color:var(--green);font-weight:800;font-size:23px;line-height:1.02;letter-spacing:.5px}

  /* headline */
  .kicker{position:absolute;left:64px;top:152px;font-weight:700;font-size:18px;line-height:1.02;color:var(--ink);letter-spacing:.2px}
  .kicker-rule{position:absolute;left:300px;top:196px;width:255px;height:1px;background:#9a9a9a}
  .headline{position:absolute;left:50px;top:206px;width:510px;font-weight:900;line-height:.95;text-transform:uppercase}
  .headline .line-one{display:block;font-size:60px;letter-spacing:-1px}
  .headline .seven{color:var(--ink)}
  .headline .bright{color:var(--green)}
  .headline .line-two{display:block;font-size:70px;color:var(--orange);text-align:right;letter-spacing:-1px}
  .tagline{position:absolute;left:168px;top:336px;width:388px;height:30px;background:var(--green);transform:skewX(-8deg);display:flex;align-items:center;justify-content:center}
  .tagline span{transform:skewX(8deg);color:var(--yellow);font-weight:700;font-size:14px;letter-spacing:.3px}

  .farm-scene{position:absolute;left:178px;top:380px;width:370px;height:108px;background:linear-gradient(180deg,var(--cream) 0%,#d6e2d6 60%,#b9cfbd 100%);border-radius:4px}

  .heritage{position:absolute;left:176px;top:496px;display:flex;gap:10px;align-items:stretch}
  .heritage p{font-size:9.5px;line-height:1.15;text-transform:uppercase}
  .heritage .past{color:var(--grey);font-weight:500}
  .heritage .future{color:var(--ink);font-weight:800;border-left:1px solid #9a9a9a;padding-left:10px}

  /* priorities */
  .priority-panel{position:absolute;left:690px;top:0;width:510px;height:542px;background:var(--green)}
  .priority-list{position:absolute;left:604px;top:0;width:560px;list-style:none}
  .priority{position:absolute;left:0;width:560px;height:90px;display:flex;align-items:center}
  .priority .num{width:52px;text-align:center;font-family:"Oswald",sans-serif;font-weight:700;font-size:66px;color:var(--green);line-height:1}
  .priority .icon{margin-left:50px;width:64px;height:64px;border-radius:50%;background:var(--white);display:flex;align-items:center;justify-content:center;flex:none}
  .priority .icon svg{width:40px;height:40px;fill:none;stroke:var(--orange);stroke-width:2;stroke-linecap:round;stroke-linejoin:round}
  .priority .copy{margin-left:28px;font-family:"Oswald",sans-serif;text-transform:uppercase}
  .priority h3{color:var(--white);font-weight:600;font-size:22px;line-height:1.1;letter-spacing:.2px}
  .priority p{color:var(--yellow);font-weight:500;font-size:15.5px;line-height:1.2;margin-top:3px}
  .divider{position:absolute;left:10px;width:546px;height:2px;background:var(--orange)}

  /* footer */
  .footer-band{position:absolute;left:0;top:542px;width:1200px;height:58px;background:var(--orange);display:flex;align-items:center;justify-content:center;gap:16px}
  .footer-band .motto{color:var(--white);font-weight:800;font-size:22px;letter-spacing:.4px}
  .footer-band .sep{width:2px;height:26px;background:var(--green)}
  .footer-band .signoff{font-family:"Kalam",cursive;color:var(--green-deep);font-size:22px}
</style>
</head>
<body>
<main class="board">
  <div class="brand-disc"></div>
  <div class="brand-name">BROOKVALE<br>FOODS</div>

  <p class="kicker">FROM CHEESEMAKERS<br>TO CHANGEMAKERS:</p>
  <div class="kicker-rule"></div>
  <h1 class="headline">
    <span class="line-one"><span class="seven">Seven</span> <span class="bright">Bright</span></span>
    <span class="line-two">Paths</span>
  </h1>
  <div class="tagline"><span>FIVE PRIORITIES. ONE FUTURE.</span></div>

  <div class="farm-scene" role="img" aria-label="Line illustration of a dairy farm with barns, silo, fields and grazing cows"></div>

  <div class="heritage">
    <p class="past">Proud of our heritage.<br>Focused on our future</p>
    <p class="future">From farm to fork.<br>We're shaping the industry.</p>
  </div>

  <div class="priority-panel"></div>
  <ol class="priority-list">
    <li class="priority" style="top:54px">
      <span class="num">1</span>
      <span class="icon"><svg viewBox="0 0 40 40"><circle cx="20" cy="10" r="4"/><circle cx="10" cy="14" r="3"/><circle cx="30" cy="14" r="3"/><path d="M13 22c0-4 3-6 7-6s7 2 7 6M4 24c0-3 2-5 6-5M36 24c0-3-2-5-6-5"/><path d="M20 34c-4-1-6-4-6-8 4 0 6 3 6 8zM20 34c4-1 6-4 6-8-4 0-6 3-6 8z"/></svg></span>
      <div class="copy"><h3>People, Places &amp; Products</h3><p>We do things the right way</p></div>
    </li>
    <li class="divider" style="top:151px"></li>
    <li class="priority" style="top:154px">
      <span class="num">2</span>
      <span class="icon"><svg viewBox="0 0 40 40"><path d="M20 4l13 5v10c0 8-6 14-13 17C13 33 7 27 7 19V9z"/><rect x="14" y="18" width="12" height="9" rx="1"/><path d="M16 18v-3a4 4 0 018 0v3"/></svg></span>
      <div class="copy"><h3>Cyber Security</h3><p>Protecting what matters</p></div>
    </li>
    <li class="divider" style="top:249px"></li>
    <li class="priority" style="top:251px">
      <span class="num">3</span>
      <span class="icon"><svg viewBox="0 0 40 40"><circle cx="20" cy="16" r="11"/><circle cx="20" cy="16" r="7"/><path d="M20 12l1.3 2.7 3 .4-2.2 2 .6 3-2.7-1.5-2.7 1.5.6-3-2.2-2 3-.4z"/><path d="M13 25l-4 10 5-2 3 4 3-8M27 25l4 10-5-2-3 4-3-8"/></svg></span>
      <div class="copy"><h3>Quality &amp; Continuous Improvement</h3><p>Be the best at what we do</p></div>
    </li>
    <li class="divider" style="top:346px"></li>
    <li class="priority" style="top:349px">
      <span class="num">4</span>
      <span class="icon"><svg viewBox="0 0 40 40"><circle cx="20" cy="12" r="5"/><circle cx="9" cy="16" r="4"/><circle cx="31" cy="16" r="4"/><path d="M11 32v-4c0-5 4-8 9-8s9 3 9 8v4zM3 32v-3c0-4 2-6 6-6M37 32v-3c0-4-2-6-6-6"/></svg></span>
      <div class="copy"><h3>Customer Focus</h3><p>Build trust. Create value. For the long term.</p></div>
    </li>
    <li class="divider" style="top:444px"></li>
    <li class="priority" style="top:447px">
      <span class="num">5</span>
      <span class="icon"><svg viewBox="0 0 40 40"><path d="M14 24a9 9 0 1112 0c-1 1-2 3-2 5h-8c0-2-1-4-2-5z"/><path d="M16 33h8M17 37h6M20 29v-8l-3-3M20 21l3-3"/><path d="M4 15h3M33 15h3M8 5l2 2M32 5l-2 2M20 1v2"/></svg></span>
      <div class="copy"><h3>Transformation &amp; Innovation</h3><p>Shaping tomorrow, today</p></div>
    </li>
  </ol>

  <footer class="footer-band">
    <span class="motto">ONE BUSINESS. ONE PURPOSE. FIVE PRIORITIES.</span>
    <span class="sep"></span>
    <span class="signoff">Let's thrive together.</span>
  </footer>
</main>
</body>
</html>
```